KORVAN TECH LTD

Advertisement to get more schools:
use website https://www.korvan-tech.co.uk for logos etc.
ICT Service Level Agreements for as little as £2000 per year
Unlimited Remote, phone and email support
Unlimited Call outs included
90% fix time within 30 minutes of ticket submission
Extra support during Quadrel inspections
GDPR service included

```html
<!DOCTYPE html>
<html lang="en">
<head>
<meta charset="utf-8">
<title>Korvan Tech – ICT SLA Agreements</title>
<link rel="stylesheet" href="https://fonts.googleapis.com/css2?family=Oswald:wght@600&family=Poppins:wght@400;500;600;700;800&display=swap">
<style>
  :root{
    --bg:#cfcfcf;
    --white:#ffffff;
    --blue:#0a72bb;
    --blue-dark:#0b4f8a;
    --sky:#eef4fb;
    --orange:#f07c45;
    --orange-soft:#f6d6c6;
    --ink:#111111;
    --photo-a:#8aa27a;
    --photo-b:#3b4a5a;
  }
  *{box-sizing:border-box;margin:0;padding:0}
  html,body{width:1200px;height:2256px;overflow:hidden;background:var(--bg)}
  body{position:relative;font-family:"Poppins",sans-serif;color:var(--ink)}
  .flyer{position:absolute;left:125px;top:264px;width:951px;height:1726px;background:var(--white);overflow:hidden}
  .abs{position:absolute}

  .brand{left:0;width:100%;top:86px;text-align:center}
  .brand-name{font-weight:700;font-size:56px;line-height:1;color:var(--orange);letter-spacing:1px}

  .hero{left:0;top:240px;width:100%;height:420px;background:var(--sky)}
  .hero-line{position:absolute;left:101px;line-height:1;white-space:nowrap}
  .h-get{top:38px;font-size:46px;font-weight:400}
  .h-ict{top:82px;font-family:"Oswald",sans-serif;font-weight:600;font-size:100px;color:var(--blue);letter-spacing:1px}
  .h-agree{top:186px;font-size:47px;font-weight:700;letter-spacing:-.5px}
  .h-little{top:237px;font-size:39px;font-weight:400}
  .h-price{top:277px;font-size:104px;font-weight:800;color:var(--orange);letter-spacing:-2px}
  .h-year{top:380px;font-size:33px;font-weight:700;color:var(--blue)}
  .hero-photo{left:454px;top:2px;width:391px;height:418px;border:6px solid var(--orange);border-radius:32px;background:linear-gradient(135deg,var(--photo-a),var(--photo-b))}

  .unlimited-frame{left:161px;top:710px;width:626px;height:520px;border:3px solid var(--blue);border-bottom:none}
  .unlimited-title{left:0;width:100%;top:684px;text-align:center}
  .unlimited-title span{display:inline-block;background:var(--white);padding:0 10px;font-size:37px;font-weight:700;color:var(--blue);letter-spacing:7px}

  .connectors{left:0;top:0}
  .service-icon{width:140px;height:140px;border-radius:50%;background:var(--orange);box-shadow:0 0 0 8px var(--orange-soft);display:flex;align-items:center;justify-content:center}
  .service-pill{width:283px;height:55px;border:3px solid var(--orange);border-radius:16px 30px 0 16px;font-size:31px;font-weight:500;display:flex;align-items:center;padding-left:24px;background:var(--white)}

  .features{left:0;top:1224px;width:100%;height:316px;background:var(--sky);border-top:3px solid var(--blue)}
  .feature-tile{width:151px;height:116px;background:var(--blue);box-shadow:4px -4px 0 var(--blue-dark);display:flex;align-items:center;justify-content:center}
  .feature-label{height:43px;background:var(--orange);color:var(--white);font-weight:800;font-size:25px;display:flex;align-items:center;justify-content:center;border-radius:0 0 12px 12px;white-space:nowrap}
  .feature-text{width:300px;text-align:center;font-size:25px;line-height:31px}
  .gdpr{left:390px;top:1294px;width:172px;height:172px;border-radius:50%;background:var(--orange);box-shadow:0 0 0 8px var(--orange-soft);color:var(--white);text-align:center;display:flex;flex-direction:column;justify-content:center;font-weight:700;line-height:1.05}
  .gdpr b{font-size:32px}
  .gdpr .s{font-size:30px;font-weight:600}
  .gdpr .i{font-size:22px;font-weight:600}

  .footer{left:0;top:1540px;width:100%;height:186px;background:var(--blue);color:var(--white)}
  .footer-bar{left:101px;top:56px;width:4px;height:54px;background:var(--white)}
  .footer-visit{left:121px;top:54px;font-size:20px;font-weight:600}
  .footer-url{left:121px;top:80px;font-size:30px;font-weight:700}
  .footer-follow{left:701px;top:52px;font-size:20px;font-weight:600}
  .social{left:697px;top:80px;display:flex;gap:10px}
  .social i{display:block;width:32px;height:32px;border:2px solid var(--white);border-radius:50%}
</style>
</head>
<body>
<main class="flyer">
  <header class="brand abs">
    <div class="brand-name">KORVAN TECH</div>
  </header>

  <section class="hero abs">
    <div class="hero-line h-get">GET YOUR</div>
    <div class="hero-line h-ict">ICT SLA</div>
    <div class="hero-line h-agree">AGREEMENTS</div>
    <div class="hero-line h-little">FOR AS LITTLE AS</div>
    <div class="hero-line h-price">£2000</div>
    <div class="hero-line h-year">PER YEAR</div>
    <div class="hero-photo abs" role="img" aria-label="Photo of school pupils working at laptops in a bright classroom"></div>
  </section>

  <div class="unlimited-frame abs"></div>
  <h2 class="unlimited-title abs"><span>UNLIMITED</span></h2>

  <svg class="connectors abs" width="951" height="1230" aria-hidden="true">
    <path d="M302 908 V928 H660 V914" fill="none" stroke="var(--orange-soft)" stroke-width="3" stroke-dasharray="9 7"/>
    <path d="M660 1054 V1098 H302 V1061" fill="none" stroke="var(--orange-soft)" stroke-width="3" stroke-dasharray="9 7"/>
  </svg>

  <div class="service-icon abs" style="left:232px;top:768px">
    <svg width="80" height="80" viewBox="0 0 80 80" fill="none" stroke="#fff" stroke-width="3"><rect x="6" y="8" width="32" height="22" rx="2"/><path d="M16 36h12M22 30v6"/><rect x="40" y="42" width="32" height="22" rx="2"/><path d="M50 70h12M56 64v6"/><path d="M46 12h12v12M54 20l4 4 4-4M34 58H22V46M26 50l-4-4-4 4"/><circle cx="40" cy="38" r="7"/></svg>
  </div>
  <div class="service-pill abs" style="left:404px;top:799px">Remote</div>

  <div class="service-pill abs" style="left:255px;top:966px">Email Support</div>
  <div class="service-icon abs" style="left:590px;top:914px">
    <svg width="80" height="80" viewBox="0 0 80 80" fill="none" stroke="#fff" stroke-width="3"><path d="M8 36v32h64V36L40 58z"/><path d="M8 36l32 22 32-22"/><path d="M20 44V10h32l8 8v26"/><circle cx="40" cy="28" r="9"/></svg>
  </div>

  <div class="service-icon abs" style="left:232px;top:1061px">
    <svg width="80" height="80" viewBox="0 0 80 80" fill="none" stroke="#fff" stroke-width="3"><rect x="22" y="6" width="34" height="68" rx="5"/><path d="M34 66h10"/><path d="M60 28c4 4 4 12 0 16M66 24c6 7 6 17 0 24"/><path d="M32 26c0 10 8 20 16 22l4-5-6-4-3 3c-3-2-5-5-6-8l3-3-4-6z"/></svg>
  </div>
  <div class="service-pill abs" style="left:404px;top:1134px">Call Outs</div>

  <section class="features abs"></section>

  <div class="feature-tile abs" style="left:152px;top:1264px">
    <svg width="100" height="70" viewBox="0 0 100 70" fill="none" stroke="#fff" stroke-width="3"><rect x="6" y="8" width="36" height="52" rx="3"/><path d="M14 20l3 3 5-6M14 34l3 3 5-6M14 48l3 3 5-6M28 20h8M28 34h8M28 48h8"/><circle cx="46" cy="50" r="10"/><path d="M46 44v6h5"/><path d="M60 30l18-12 14 20-18 12z"/></svg>
  </div>
  <div class="feature-label abs" style="left:133px;top:1387px;width:206px">90% FIX TIME</div>
  <p class="feature-text abs" style="left:92px;top:1460px">within 30 minutes<br>of ticket submission</p>

  <div class="gdpr abs"><b>GDPR</b><span class="s">SERVICE</span><span class="i">INCLUDED</span></div>

  <div class="feature-tile abs" style="left:634px;top:1264px">
    <svg width="90" height="80" viewBox="0 0 90 80" fill="none" stroke="#fff" stroke-width="3"><rect x="8" y="8" width="60" height="54" rx="3"/><path d="M16 20h16M16 28h12M18 54V44M26 54V38M34 54V46"/><path d="M36 32l10-8 8 6 12-14"/><circle cx="68" cy="14" r="4"/><circle cx="56" cy="54" r="12"/><circle cx="56" cy="54" r="5"/></svg>
  </div>
  <div class="feature-label abs" style="left:584px;top:1387px;width:264px">EXTRA SUPPORT</div>
  <p class="feature-text abs" style="left:569px;top:1460px">during Quadrel<br>inspections</p>

  <footer class="footer abs">
    <div class="footer-bar abs"></div>
    <div class="footer-visit abs">Please visit our website</div>
    <div class="footer-url abs">www.korvan-tech.co.uk</div>
    <div class="footer-follow abs">Follow Us</div>
    <div class="social abs" aria-label="Social media links"><i></i><i></i><i></i></div>
  </footer>
</main>
</body>
</html>
```